Awesome Digital Ad Design – Pellucid Adreach

I am going to be setting up a Pellucid Adreach ad campaign I need creatives for.

Several sizes are needed in the end, however, please submit your design concept in the following 2 sizes to start:
Medium rectangle: 300X250
Leaderboard: 728X90

Original artwork/design files and images used expected upon payment and as part of the final delivery.

Ads should match our company brand and the information on this webpage: http://www.harborlyneworks.com/real-estate-marketing/
SEE MORE INSTRUCTIONS IN ATTACHED WORD DOC
Updates

Target Market(s)

Business-To-Business Audience –Real Estate Company Executives (Presidents/VPs/Owners/CEOs/Sales Managers).

Industry/Entity Type

Real Estate

Font styles to use
Sans Serif

Requirements
Must have
• Copy should be minimal words, billboard like. Please use real photos/images that would appeal to real estate high-level decision-maker executives.
Should not have
• No cartoons or graphics

```html
<!DOCTYPE html>
<html lang="en">
<head>
<meta charset="utf-8">
<title>Harborlyne Works – Pellucid Adreach Ad Set</title>
<link rel="stylesheet" href="https://fonts.googleapis.com/css2?family=Arimo:ital,wght@0,400;0,700;1,700&display=swap">
<style>
  :root {
    --page: #ffffff;
    --ink: #111111;
    --tan-light: #d6cb9c;
    --tan-dark: #a99d6c;
    --slate-dark: #383838;
    --slate-light: #6d6d6d;
    --steel-blue: #4a78a6;
    --steel-blue-dark: #1f4f86;
    --maroon: #7d2a30;
    --orange-light: #fb8f34;
    --orange-dark: #e0580b;
    --orange-deep: #a8400a;
    --logo-grey: #5e6670;
    --frame: #c8c8c8;
  }
  * { margin: 0; padding: 0; box-sizing: border-box; }
  html, body { width: 1200px; height: 1200px; overflow: hidden; background: var(--page); }
  body { font-family: "Arimo", Arial, sans-serif; color: var(--ink); }

  .board {
    position: absolute; left: 0; top: 0;
    width: 850px; height: 850px;
    transform: scale(1.41176); transform-origin: 0 0;
  }
  .ad { position: absolute; overflow: hidden; border: 1px solid var(--frame); background: #fff; }
  .ad svg.ad-art { position: absolute; left: 0; top: 0; }
  .size-label {
    position: absolute; width: 200px; text-align: center;
    font-size: 17px; font-weight: 400; letter-spacing: .5px;
  }

  .offer {
    position: absolute; color: #fff; font-weight: 700; font-style: italic;
    text-shadow: 1px 1px 2px rgba(0,0,0,.7); line-height: 1;
  }
  .headline {
    position: absolute; color: #fff; font-weight: 700;
    text-shadow: 1px 1px 1px rgba(0,0,0,.55); line-height: 1.08;
  }
  .brand {
    position: absolute; display: flex; align-items: center; gap: 3px;
    color: var(--logo-grey); font-size: 9px; font-weight: 400; line-height: 1.15;
  }
  .brand-dot { width: 7px; height: 7px; border-radius: 50%; background: var(--logo-grey); flex: none; }

  .cta {
    position: absolute; display: flex; align-items: center; justify-content: center; gap: 6px;
    background: linear-gradient(var(--orange-light), var(--orange-dark));
    border-radius: 3px; border-bottom: 3px solid var(--orange-deep);
    color: #fff; font-weight: 700; text-shadow: 1px 1px 1px rgba(0,0,0,.6);
    box-shadow: 0 1px 2px rgba(0,0,0,.35);
  }
  .cta-icon {
    width: 20px; height: 20px; border-radius: 50%;
    background: var(--orange-deep); border: 1px solid #f9b27a;
    display: flex; align-items: center; justify-content: center; flex: none;
  }

  /* Leaderboard */
  .leaderboard { left: 60px; top: 185px; width: 728px; height: 90px; }
  .leaderboard .offer { left: 8px; top: 15px; width: 170px; text-align: center; font-size: 19px; }
  .leaderboard .headline { left: 205px; top: 13px; font-size: 19px; }
  .leaderboard .brand { left: 402px; top: 38px; }
  .leaderboard .cta { left: 462px; top: 38px; width: 118px; height: 42px; font-size: 12px; }

  /* Medium rectangle */
  .rectangle { left: 265px; top: 354px; width: 300px; height: 250px; }
  .rectangle .offer { left: 0; top: 4px; width: 300px; text-align: center; font-size: 19px; }
  .rectangle .headline { left: 6px; top: 74px; font-size: 19px; line-height: 1.3; }
  .rectangle .brand { left: 14px; top: 200px; }
  .rectangle .cta { left: 138px; top: 199px; width: 135px; height: 46px; font-size: 13px; }
</style>
</head>
<body>
<div class="board">

  <section class="ad leaderboard" aria-label="728 by 90 leaderboard ad">
    <svg class="ad-art" width="728" height="90" viewBox="0 0 728 90">
      <defs>
        <linearGradient id="lb-tan" x1="0" y1="0" x2="0" y2="1">
          <stop offset="0" stop-color="var(--tan-light)"/><stop offset="1" stop-color="var(--tan-dark)"/>
        </linearGradient>
        <linearGradient id="lb-slate" x1="0" y1="0" x2="1" y2="0">
          <stop offset="0" stop-color="var(--slate-dark)"/><stop offset="1" stop-color="var(--slate-light)"/>
        </linearGradient>
        <linearGradient id="lb-blue" x1="0" y1="0" x2="1" y2="0">
          <stop offset="0" stop-color="var(--steel-blue-dark)"/><stop offset="1" stop-color="var(--steel-blue)"/>
        </linearGradient>
        <linearGradient id="lb-photo" x1="0" y1="0" x2="1" y2="1">
          <stop offset="0" stop-color="#8fa7c4"/><stop offset=".5" stop-color="#d8d3c6"/><stop offset="1" stop-color="#6b4a4e"/>
        </linearGradient>
      </defs>
      <rect width="728" height="90" fill="#fff"/>
      <path d="M178,0 H412 L345,90 H178 Z" fill="url(#lb-slate)"/>
      <path d="M418,0 H728 V14 H600 Q520,14 430,8 Z" fill="url(#lb-blue)"/>
      <path d="M412,0 H424 L362,80 Q358,84 372,84 H590 Q615,84 640,90 H345 Z" fill="var(--maroon)"/>
      <path d="M590,0 H728 V90 H655 Q612,84 600,50 Q594,25 590,0 Z" fill="url(#lb-photo)"
            role="img" aria-label="Photo of a smiling real estate agent holding a sold sign in front of a modern home"/>
      <path d="M0,0 H172 Q198,45 172,90 H0 Z" fill="url(#lb-tan)"/>
      <path d="M172,0 Q198,45 172,90 H180 Q206,45 180,0 Z" fill="var(--steel-blue)"/>
    </svg>
    <p class="offer">Virtually<br>No Cost To<br>Your Company!</p>
    <h2 class="headline">Client Follow-up<br>&amp; Prospecting<br>Made simple</h2>
    <div class="brand"><span class="brand-dot"></span><span>Harborlyne<br>Works</span></div>
    <a class="cta">LEARN MORE!
      <span class="cta-icon"><svg width="8" height="9" viewBox="0 0 8 9"><path d="M1,0 L8,4.5 L1,9 Z" fill="#fff"/></svg></span>
    </a>
  </section>
  <p class="size-label" style="left:324px; top:290px;">728X90</p>

  <section class="ad rectangle" aria-label="300 by 250 medium rectangle ad">
    <svg class="ad-art" width="300" height="250" viewBox="0 0 300 250">
      <defs>
        <linearGradient id="mr-tan" x1="0" y1="0" x2="0" y2="1">
          <stop offset="0" stop-color="var(--tan-light)"/><stop offset="1" stop-color="var(--tan-dark)"/>
        </linearGradient>
        <linearGradient id="mr-slate" x1="0" y1="0" x2="1" y2="0">
          <stop offset="0" stop-color="var(--slate-dark)"/><stop offset="1" stop-color="var(--slate-light)"/>
        </linearGradient>
        <linearGradient id="mr-photo" x1="0" y1="0" x2="1" y2="1">
          <stop offset="0" stop-color="#a9b7c6"/><stop offset=".5" stop-color="#dcd6c8"/><stop offset="1" stop-color="#5e3f46"/>
        </linearGradient>
      </defs>
      <rect width="300" height="250" fill="#fff"/>
      <path d="M0,0 H300 V40 Q150,46 0,40 Z" fill="url(#mr-tan)"/>
      <path d="M0,40 Q150,46 300,40 V58 H0 Z" fill="var(--steel-blue)"/>
      <path d="M0,58 H300 V190 H0 Z" fill="url(#mr-slate)"/>
      <path d="M195,58 H300 V190 H125 Z" fill="url(#mr-photo)"
            role="img" aria-label="Photo of a smiling real estate agent holding a sold sign in front of a modern home"/>
      <path d="M190,58 H200 L125,186 H300 V196 H112 Z" fill="var(--maroon)"/>
      <path d="M0,176 Q60,178 100,184 L112,196 H0 Z" fill="var(--maroon)"/>
      <path d="M0,186 Q60,188 100,192 L108,196 H0 Z" fill="#fff" opacity=".6"/>
    </svg>
    <p class="offer">Virtually No Cost To<br>Your Company!</p>
    <h2 class="headline">Client Follow-up<br>&amp; Prospecting<br>Made simple</h2>
    <div class="brand"><span class="brand-dot"></span><span>Harborlyne<br>Works</span></div>
    <a class="cta">LEARN MORE!
      <span class="cta-icon"><svg width="8" height="9" viewBox="0 0 8 9"><path d="M1,0 L8,4.5 L1,9 Z" fill="#fff"/></svg></span>
    </a>
  </section>
  <p class="size-label" style="left:315px; top:622px;">300X250</p>

</div>
</body>
</html>
```